Ecommerce Web Design - We currently have a live website running on https://www.brivanto.co.za - this website must be redesigned for an eCommerce website since we are moving to sell our items online. Kindly put a new design utilising the information from the current live website

Link to Pictures & Brochure: https://tolvesta-my.filedrop.example/:f:/g/personal/dumisa_paterlo_co_za/QxpLMrtVwaUeHbnKd3ZPoeyT-RUI8gHjNtwXZCF7pBLAmv?e=kR4z91

```html
<!DOCTYPE html>
<html lang="en">
<head>
<meta charset="utf-8">
<title>Brivanto – Ladders, Trolleys &amp; Castors</title>
<link rel="stylesheet" href="https://fonts.googleapis.com/css2?family=Poppins:ital,wght@0,300;0,400;0,500;0,600;0,700;0,800;1,300&display=swap">
<style>
:root{
  --blue:#0b4ea2;
  --ink:#1b1b1b;
  --muted:#6d6d6d;
  --light:#f3f3f3;
  --line:#e4e4e4;
  --dark:#141414;
  --gold:#f2b411;
  --white:#fff;
}
*{box-sizing:border-box;margin:0;padding:0}
html,body{width:1200px;height:3665px;overflow:hidden}
body{font-family:"Poppins",sans-serif;color:var(--ink);background:var(--white);font-size:11px}
.wrap{width:882px;margin:0 auto;position:relative}
.btn{display:inline-flex;align-items:center;gap:8px;background:var(--blue);color:#fff;border-radius:20px;font-size:9px;font-weight:500;padding:6px 14px;text-decoration:none;white-space:nowrap}
.btn::after{content:"›";font-size:12px;line-height:1}
.sec-title{text-align:center;font-size:17px;font-weight:500;letter-spacing:.2px}
.sec-title b{color:var(--blue);font-weight:600}
.sec-sub{text-align:center;color:var(--muted);font-size:8.5px;line-height:15px;width:420px;margin:6px auto 0}
.arrow-btn{position:absolute;width:34px;height:34px;border-radius:50%;background:#e2e2e2;border:none;color:#fff;font-size:18px;display:flex;align-items:center;justify-content:center}

.topbar{height:34px;border-bottom:1px solid var(--line)}
.topbar .wrap{display:flex;justify-content:space-between;align-items:center;height:34px;font-size:9px}
.topbar b{font-weight:600}
.topbar span{color:var(--muted)}
.top-right{display:flex;gap:26px;align-items:center;color:var(--muted)}
.top-right .cart{display:flex;gap:6px;align-items:center;line-height:10px}
.cart small{font-size:7px;display:block}
.cart strong{color:var(--blue);font-weight:600;font-size:9px}

.header{height:80px;border-bottom:1px solid var(--line)}
.header .wrap{display:flex;align-items:center;height:80px}
.brand{display:flex;align-items:center;gap:6px;font-weight:700;font-size:13px;color:var(--blue);width:150px}
.brand i{width:14px;height:14px;background:var(--blue);display:block}
.nav{display:flex;gap:30px;font-size:9px;font-weight:500;flex:1}
.search{width:26px;height:26px;border-radius:50%;background:var(--blue);display:flex;align-items:center;justify-content:center;margin-right:14px}
.livechat{border:2px solid var(--blue);border-radius:8px;padding:4px 10px;display:flex;gap:8px;align-items:center;line-height:11px}
.livechat small{font-size:7.5px;display:block}
.livechat strong{color:var(--blue);font-size:12px;font-weight:600}

.hero{height:505px;position:relative;background:linear-gradient(90deg,#cfcfcf 0%,#ececec 30%,#f1f1f1 55%,#dcdcdc 80%,#cacaca 100%);text-align:center}
.hero .veil{position:absolute;inset:0;background:rgba(255,255,255,.55)}
.hero-in{position:relative;padding-top:180px}
.hero .eyebrow{font-size:14px}
.hero h1{font-size:42px;font-weight:400;letter-spacing:.5px;margin-top:2px}
.hero h1 b{color:var(--blue);font-weight:800}
.hero p{font-size:13.5px;line-height:20px;margin-top:8px}
.hero .btn{margin-top:30px}
.dots{display:flex;gap:8px;justify-content:center;margin-top:30px;align-items:center}
.dots i{width:10px;height:10px;border-radius:50%;background:#111;display:block}
.dots i.on{background:transparent;border:1.5px solid var(--blue);width:14px;height:14px}
.hero .chev{position:absolute;top:240px;font-size:40px;font-weight:200;color:#333}

.promos{height:316px;padding-top:57px}
.promos .wrap{display:flex;gap:19px}
.promo{flex:1;height:168px;background:#f3f3f3;border-radius:6px;display:flex;align-items:center;padding:0 16px;justify-content:space-between}
.promo small{font-size:8.5px;display:block;margin-bottom:2px}
.promo h3{color:var(--blue);font-size:13px;font-weight:600;line-height:16px;white-space:nowrap}
.promo h3.two{white-space:normal;width:125px}
.promo p{font-size:8.5px;margin-top:5px}
.promo .btn{margin-top:12px}
.ph{border-radius:4px}
.promo .ph{width:70px;height:130px;background:linear-gradient(160deg,#c9d7ec,#7ea0d1);flex:none}

.about{height:481px;padding-top:59px}
.about .wrap{display:flex;gap:20px}
.about-img{width:355px;height:341px;border-bottom:4px solid var(--blue);border-right:4px solid var(--blue);border-radius:10px;background:linear-gradient(150deg,#9fb4cf,#e2c48f 40%,#5f7ea5 75%,#3a4d6d);flex:none}
.about-text{flex:1}
.about h2{font-size:17px;font-weight:600;margin-top:4px}
.about h2 b{color:var(--blue)}
.about-text>p{font-size:9.5px;color:var(--muted);line-height:16px;margin-top:6px}
.pillar{display:flex;gap:14px;margin-top:22px}
.pillar .ico{width:52px;height:52px;border-radius:50%;background:var(--blue);flex:none;display:flex;align-items:center;justify-content:center}
.pillar h4{font-size:13.5px;font-weight:500}
.pillar p{font-size:8.5px;color:var(--muted);line-height:15px;margin-top:2px}
.about .btn{margin:22px 0 0 57px}

.categories{height:381px;background:var(--light);padding-top:52px}
.cat-row{display:flex;gap:19px;margin-top:36px}
.cat{width:131px;height:162px;background:#fff;border:1px solid #d6d6d6;border-radius:6px;text-align:center;padding-top:10px}
.cat .ph{width:90px;height:96px;margin:0 auto;background:linear-gradient(160deg,#d5e0f1,#5f86c4)}
.cat .ph.y{background:linear-gradient(160deg,#fbe4a0,#e4a11f)}
.cat .ph.g{background:linear-gradient(160deg,#e4e4e4,#9aa3ad)}
.cat h5{font-size:9.5px;font-weight:500;margin:8px 0 8px}
.categories .arrow-btn{top:204px}

.products{height:513px;padding-top:52px}
.prod-row{display:flex;gap:19px;margin-top:36px}
.prod{width:206px;height:277px;border:1px solid var(--line);border-radius:6px;padding:9px;text-align:center}
.prod.active{box-shadow:0 4px 14px rgba(0,0,0,.12)}
.prod .img{height:174px;background:#f0f0f0;border-radius:5px;position:relative;display:flex;align-items:center;justify-content:center}
.prod .img .ph{width:100px;height:150px;background:linear-gradient(160deg,#dfe7f3,#6b8fc8)}
.prod .img .ph.w{width:150px;height:90px}
.prod .img .ph.s{background:linear-gradient(160deg,#eaeaea,#9ba4ad);width:150px;height:110px}
.badge{position:absolute;left:8px;top:9px;background:var(--blue);color:#fff;font-size:7px;padding:1px 6px;border-radius:2px}
.cartbar{position:absolute;left:0;right:0;bottom:4px;margin:0 auto;width:170px;background:var(--blue);color:#fff;font-size:9px;font-weight:500;border-radius:14px;padding:6px 0}
.stars{color:var(--gold);font-size:10px;letter-spacing:2px;margin-top:11px}
.prod h5{color:var(--blue);font-size:9.5px;font-weight:500;margin-top:5px}
.prod p{font-size:8px;margin-top:3px}
.price{color:var(--blue);font-size:12px;font-weight:600;margin-top:9px}
.price s{color:#999;font-size:8px;font-weight:400;margin-left:4px}
.products .arrow-btn{top:209px}

.banner{height:234px;background:linear-gradient(90deg,#2f6db8,#4f85c6 55%,#3e74b9);color:#fff}
.banner .wrap{width:1060px;display:flex;justify-content:space-between;align-items:center;height:234px}
.banner h2{font-size:25px;font-weight:700}
.banner p{font-size:14px;font-weight:500;margin-top:6px}
.btn-dark{background:#111;color:#fff;border-radius:20px;font-size:9px;padding:8px 16px;margin-right:123px}

.why{height:289px;background:var(--light);padding-top:56px}
.features{display:flex;justify-content:space-between;margin-top:30px;padding:0 50px 0 70px}
.feature{text-align:center;width:200px}
.feature .ico{width:57px;height:57px;border-radius:50%;background:var(--blue);margin:0 auto;display:flex;align-items:center;justify-content:center}
.feature h5{font-size:10px;font-weight:500;margin-top:16px}
.feature p{font-size:8.5px;color:var(--muted);margin-top:2px}

.testimonials{height:431px;padding-top:62px}
.testi-row{display:flex;gap:19px;margin-top:40px}
.testi{width:281px;height:199px;background:#f6f6f6;border-radius:6px;padding:14px 14px}
.testi .top{display:flex;justify-content:space-between}
.avatar{width:52px;height:52px;border-radius:50%;border:2px solid var(--blue);background:linear-gradient(160deg,#e8c8a8,#9a6b4b)}
.testi .who{text-align:center;margin-right:22px}
.who h5{font-size:10px;font-weight:600}
.who small{color:var(--blue);font-size:7.5px;display:block}
.who i{color:var(--gold);font-size:9px;font-style:normal;letter-spacing:1px}
.testi p{font-size:8.5px;font-style:italic;font-weight:300;color:var(--muted);line-height:15px;margin-top:6px}
.quote{text-align:center;font-size:46px;color:#cfcfcf;font-weight:700;line-height:40px;margin-top:2px}
.testimonials .arrow-btn{top:225px}

.footer{height:263px;background:var(--dark);color:#fff;padding-top:52px}
.footer .wrap{display:flex;width:870px}
.f-brand{width:300px}
.f-brand .brand{color:#fff;margin-bottom:28px}
.f-brand p{font-size:10.5px;line-height:19px}
.pay{display:flex;gap:5px;margin-top:12px}
.pay i{width:31px;height:18px;background:#fff;border-radius:2px;display:block}
.f-col h4{color:var(--blue);font-size:15px;font-weight:500;margin-bottom:8px}
.f-col li{list-style:none;font-size:10.5px;line-height:21px}
.f-col li::before{content:"› "}
.f-contact li::before{content:""}
.f-col.links{width:200px}
.f-col.acct{width:175px}
.f-col.f-contact{width:195px}
.newsletter{height:96px;background:var(--dark);border-top:1px solid #333;color:#fff;text-align:center;padding-top:22px}
.newsletter h5{font-size:10.5px;font-weight:400}
.nl-form{width:282px;height:30px;background:#fff;border-radius:16px;margin:10px auto 0;display:flex;justify-content:space-between;align-items:center;padding-left:18px;overflow:hidden}
.nl-form span{color:#999;font-size:8px}
.nl-form b{background:var(--blue);height:30px;line-height:30px;padding:0 16px;border-radius:16px;font-size:9px;font-weight:500}
.bottom{height:42px;background:var(--blue);color:#fff}
.bottom .wrap{display:flex;justify-content:space-between;align-items:center;height:42px;width:870px}
.social{display:flex;gap:10px}
.social i{width:24px;height:24px;border-radius:50%;border:1.5px solid #fff;display:block}
.bottom p{font-size:8.5px}
.bottom p mark{background:#000;color:#fff;padding:0 2px}
</style>
</head>
<body>

<div class="topbar"><div class="wrap">
  <div><b>Limited Time Offer:</b> <span>Shop online and get free no-contact delivery</span></div>
  <div class="top-right">
    <div><svg width="12" height="12" viewBox="0 0 12 12" fill="none" stroke="#0b4ea2" stroke-width="1.2"><circle cx="6" cy="4" r="2.5"/><path d="M1.5 11c0-2.5 2-4 4.5-4s4.5 1.5 4.5 4"/></svg> Login</div>
    <div class="cart"><svg width="16" height="14" viewBox="0 0 16 14" fill="none" stroke="#0b4ea2" stroke-width="1.2"><path d="M1 1h2l2 8h8l2-6H4"/><circle cx="6" cy="12" r="1"/><circle cx="12" cy="12" r="1"/></svg><div><small>My Cart</small><strong>$299.49</strong></div></div>
  </div>
</div></div>

<header class="header"><div class="wrap">
  <div class="brand"><i></i>BRIVANTO</div>
  <nav class="nav"><span>HOME</span><span>ABOUT US</span><span>PRODUCTS ⌄</span><span>SAFETY INFORMATION ⌄</span><span>DOWNLOADS</span><span>CONTACT US</span></nav>
  <div class="search"><svg width="11" height="11" viewBox="0 0 11 11" fill="none" stroke="#fff" stroke-width="1.5"><circle cx="4.5" cy="4.5" r="3.5"/><path d="M7 7l3 3"/></svg></div>
  <div class="livechat"><svg width="18" height="16" viewBox="0 0 18 16" fill="none" stroke="#0b4ea2" stroke-width="1.6"><path d="M2 10V8a7 7 0 0114 0v2"/><rect x="1" y="9" width="3" height="5" rx="1"/><rect x="14" y="9" width="3" height="5" rx="1"/></svg><div><small>Live Chat Or:</small><strong>011-482-7730</strong></div></div>
</div></header>

<section class="hero" role="img" aria-label="Photo of two women posing beside an aluminium ladder">
  <div class="veil"></div>
  <span class="chev" style="left:48px">‹</span><span class="chev" style="right:48px">›</span>
  <div class="hero-in">
    <div class="eyebrow">Best offer for you</div>
    <h1><b>FIBREGLASS</b> LADDERS</h1>
    <p>South Africa's Leading Manufacturer of Ladders, Trolleys, Castors,<br>Wheels &amp; Ladder Accessories</p>
    <a class="btn">Shop Now</a>
    <div class="dots"><i></i><i class="on"></i><i></i></div>
  </div>
</section>

<section class="promos"><div class="wrap">
  <div class="promo"><div><small>Sale 20% Off first Order</small><h3>FOLDING NOSE TROLLEY</h3><a class="btn">Shop Now</a></div><div class="ph" role="img" aria-label="Blue folding nose trolley"></div></div>
  <div class="promo"><div><h3 class="two">SMALL PLATFORM TROLLEY</h3><p>Hurry, quantities are Limited</p><a class="btn">Shop Now</a></div><div class="ph" style="height:70px;width:95px" role="img" aria-label="Small blue platform trolley"></div></div>
  <div class="promo"><div><h3>KR RANGE – HEAVY DUTY</h3><p>Hurry, quantities are Limited</p><a class="btn">Shop Now</a></div><div class="ph" style="width:45px;height:160px" role="img" aria-label="Heavy duty aluminium extension ladder"></div></div>
</div></section>

<section class="about"><div class="wrap">
  <div class="about-img" role="img" aria-label="Photo of two workers in hard hats beside a ladder reviewing plans"></div>
  <div class="about-text">
    <h2>ABOUT <b>US</b></h2>
    <p>Brivanto was founded in 1992 as a family owned manufacturing business that produces ladders. Today, we have evolved to a business that manufactures ladders, trolleys, castors, wheels, store bins, scaffolding and ladder accessories for Southern Africa and international markets.</p>
    <div class="pillar"><div class="ico"><svg width="24" height="24" viewBox="0 0 24 24" fill="none" stroke="#fff" stroke-width="1.4"><circle cx="12" cy="12" r="9"/><circle cx="12" cy="12" r="5"/><circle cx="12" cy="12" r="1.5"/></svg></div><div><h4>Vision</h4><p>To become a preferred manufacturer of ladders, trolleys, castors, wheels, store bins, scaffolding and ladder accessories by consistently delivering products that meet both national and international quality standards.</p></div></div>
    <div class="pillar"><div class="ico"><svg width="24" height="24" viewBox="0 0 24 24" fill="none" stroke="#fff" stroke-width="1.4"><circle cx="12" cy="9" r="4"/><path d="M5 20c1-4 4-6 7-6s6 2 7 6"/></svg></div><div><h4>Mission</h4><p>Brivanto strives to produce quality products for a range of consumers, taking cognisance of safety, health and environmental issues.</p></div></div>
    <div class="pillar"><div class="ico"><svg width="24" height="24" viewBox="0 0 24 24" fill="none" stroke="#fff" stroke-width="1.4"><path d="M4 14l4 5h8l4-5"/><circle cx="12" cy="8" r="3"/></svg></div><div><h4>Values</h4><p>Professionalism Accountability Transparency and Honesty</p></div></div>
    <a class="btn">Read More</a>
  </div>
</div></section>

<section class="categories"><div class="wrap">
  <h2 class="sec-title">OUR <b>CATEGORIES</b></h2>
  <p class="sec-sub">Lorem ipsum dolor sit amet, consectetur adipiscing elit, sed do eiusmod tempor incididunt ut labore et dolore magna aliqua.</p>
  <button class="arrow-btn" style="left:-18px">‹</button><button class="arrow-btn" style="right:-18px">›</button>
  <div class="cat-row">
    <div class="cat"><div class="ph" role="img" aria-label="Platform trolley"></div><h5>CATEGORY NAME</h5><a class="btn">Shop Now</a></div>
    <div class="cat"><div class="ph y" role="img" aria-label="Yellow step ladder"></div><h5>CATEGORY NAME</h5><a class="btn">Shop Now</a></div>
    <div class="cat"><div class="ph g" role="img" aria-label="Multi-purpose folding ladder"></div><h5>CATEGORY NAME</h5><a class="btn">Shop Now</a></div>
    <div class="cat"><div class="ph" role="img" aria-label="Platform trolley"></div><h5>CATEGORY NAME</h5><a class="btn">Shop Now</a></div>
    <div class="cat"><div class="ph y" role="img" aria-label="Yellow step ladder"></div><h5>CATEGORY NAME</h5><a class="btn">Shop Now</a></div>
    <div class="cat"><div class="ph" role="img" aria-label="Platform trolley"></div><h5>CATEGORY NAME</h5><a class="btn">Shop Now</a></div>
  </div>
</div></section>

<section class="products"><div class="wrap">
  <h2 class="sec-title">OUR LATEST <b>PRODUCTS</b></h2>
  <p class="sec-sub">Lorem ipsum dolor sit amet, consectetur adipiscing elit, sed do eiusmod tempor incididunt ut labore et dolore magna aliqua.</p>
  <button class="arrow-btn" style="left:-18px">‹</button><button class="arrow-btn" style="right:-18px">›</button>
  <div class="prod-row">
    <div class="prod"><div class="img"><span class="badge">-30%</span><div class="ph" role="img" aria-label="Extension ladder"></div></div><div class="stars">★★★★★</div><h5>KR RANGE – HEAVY DUTY</h5><p>3-IN-1 STEP/EXTENSION LADDER</p><div class="price">$35.00</div></div>
    <div class="prod"><div class="img"><span class="badge">-30%</span><div class="ph" role="img" aria-label="Folding nose trolley"></div></div><div class="stars">★★★★★</div><h5>TN4</h5><p>FOLDING NOSE TROLLEY</p><div class="price">$35.00<s>$55.00</s></div></div>
    <div class="prod active"><div class="img"><span class="badge">-30%</span><div class="ph w" style="margin-top:-30px" role="img" aria-label="Small platform trolley"></div><div class="cartbar">🛒 Add To Cart</div></div><div class="stars">★★★★★</div><h5>BKPT</h5><p>SMALL PLATFORM TROLLEY</p><div class="price">$35.00<s>$55.00</s></div></div>
    <div class="prod"><div class="img"><div class="ph s" role="img" aria-label="Large steel platform trolley"></div></div><div class="stars">★★★★★</div><h5>GRT</h5><p>LARGE PLATFORM TROLLEY</p><div class="price">$99.00</div></div>
  </div>
</div></section>

<section class="banner" role="img" aria-label="Photo of a smiling man giving a thumbs up, tinted blue"><div class="wrap">
  <div><h2>South Africa's&nbsp; Leading Manufacturer of</h2><p>Ladders, Trolleys, Castors, Wheels &amp; Ladder Accessories</p></div>
  <a class="btn btn-dark">Contact Us Now &nbsp;›</a>
</div></section>

<section class="why"><div class="wrap">
  <h2 class="sec-title">WHY SHOP <b>BRIVANTO</b></h2>
  <p class="sec-sub">Lorem ipsum dolor sit amet, consectetur adipiscing elit, sed do eiusmod tempor incididunt ut labore et dolore magna aliqua.</p>
  <div class="features">
    <div class="feature"><div class="ico"><svg width="28" height="22" viewBox="0 0 28 22" fill="none" stroke="#fff" stroke-width="1.5"><path d="M3 14V6h14v8M17 9h5l3 4v1"/><circle cx="8" cy="16" r="2.5"/><circle cx="20" cy="16" r="2.5"/></svg></div><h5>GET FREE SHIPPING</h5><p>Worldwide from $75</p></div>
    <div class="feature"><div class="ico"><svg width="26" height="26" viewBox="0 0 26 26" fill="none" stroke="#fff" stroke-width="1.4"><circle cx="13" cy="13" r="4"/><path d="M13 2v6M13 18v6M2 13h6M18 13h6M5 5l4 4M17 17l4 4M21 5l-4 4M9 17l-4 4"/></svg></div><h5>MULTIPLE DISTRIBUTION CENTER</h5><p>Easy Shipping</p></div>
    <div class="feature"><div class="ico"><svg width="26" height="26" viewBox="0 0 26 26" fill="none" stroke="#fff" stroke-width="1.4"><path d="M13 3l7 3v6c0 4-3 7-7 8-4-1-7-4-7-8V6z"/><path d="M9.5 12l2.5 2.5 4.5-4.5"/></svg></div><h5>LOW PRICE GUARANTEE</h5><p>Credit Cards Available</p></div>
  </div>
</div></section>

<section class="testimonials"><div class="wrap">
  <h2 class="sec-title">WHAT OUR <b>CLIENT SAYS</b></h2>
  <p class="sec-sub">Lorem ipsum dolor sit amet, consectetur adipiscing elit, sed do eiusmod tempor incididunt ut labore et dolore magna aliqua.</p>
  <button class="arrow-btn" style="left:-18px">‹</button><button class="arrow-btn" style="right:-18px">›</button>
  <div class="testi-row">
    <div class="testi"><div class="top"><div class="avatar" role="img" aria-label="Client portrait"></div><div class="who"><h5>JOHN DOE</h5><small>Project Manager</small><i>☆☆☆☆☆</i></div></div><p>Lorem ipsum dolor sit amet, consectetur adipiscing elit. Fusce molestie lacus sed aliquam lacinia. Ut luctus libero sed ultrices posuere. Nunc et dolor id elit efficitur porta pharetra vel nisl. Duis quis rhoncus mauris.</p><div class="quote">”</div></div>
    <div class="testi"><div class="top"><div class="avatar" role="img" aria-label="Client portrait"></div><div class="who"><h5>JOHN DOE</h5><small>Project Manager</small><i>☆☆☆☆☆</i></div></div><p>Lorem ipsum dolor sit amet, consectetur adipiscing elit. Fusce molestie lacus sed aliquam lacinia. Ut luctus libero sed ultrices posuere. Nunc et dolor id elit efficitur porta pharetra vel nisl. Duis quis rhoncus mauris.</p><div class="quote">”</div></div>
    <div class="testi"><div class="top"><div class="avatar" role="img" aria-label="Client portrait"></div><div class="who"><h5>JOHN DOE</h5><small>Project Manager</small><i>☆☆☆☆☆</i></div></div><p>Lorem ipsum dolor sit amet, consectetur adipiscing elit. Fusce molestie lacus sed aliquam lacinia. Ut luctus libero sed ultrices posuere. Nunc et dolor id elit efficitur porta pharetra vel nisl. Duis quis rhoncus mauris.</p><div class="quote">”</div></div>
  </div>
</div></section>

<footer>
  <div class="footer"><div class="wrap">
    <div class="f-brand"><div class="brand"><i style="background:#fff"></i>BRIVANTO</div><p>Adipiscing elit, sed do eiusmod tempor incididunt ut labore dolore magn aliqua. Ut enim ad minim veniam, quis nostrud exercitation ullamco laboris.</p><div class="pay"><i></i><i></i><i></i><i></i><i></i><i></i></div></div>
    <div class="f-col links"><h4>Quick Links</h4><ul><li>Home</li><li>About Us</li><li>Products</li><li>Support</li><li>Contact</li></ul></div>
    <div class="f-col acct"><h4>My Acount</h4><ul><li>My Orders</li><li>Terms</li><li>Privacy Policy</li><li>Downloads</li><li>Warranty</li></ul></div>
    <div class="f-col f-contact"><h4>Contact Us</h4><ul><li>✉ info@example.com</li><li>☏ 011 482 7730</li><li style="line-height:15px;padding:3px 0">⌖ Adipisicing elit, sed do<br>&nbsp;&nbsp;&nbsp;eiusmod tempor incididunt ut<br>&nbsp;&nbsp;&nbsp;labore dolore magn aliqua.</li><li>⛟ Mon-Fri, 7:00am to 9:00pm</li></ul></div>
  </div></div>
  <div class="newsletter"><h5>SUBSCRIBE OUR NEWSLETTER</h5><div class="nl-form"><span>Enter Your E-Mail</span><b>Subscribe Now</b></div></div>
  <div class="bottom"><div class="wrap">
    <div class="social"><i></i><i></i><i></i><i></i></div>
    <p>Copyright © 2022 Brivanto. All Rights Reserved | <mark>011 482 7730</mark> | contact@demo.com</p>
  </div></div>
</footer>

</body>
</html>
```